Modern Billboard Ad for Criminal Defense Firm

10.5 x 36 We're looking for something to set us apart from the local competition. Looking for sleek and modern. We're a mid-sized firm in a small market city. We want to give the artist room to be creative on this one.
Thanks

Target Market(s)

Adult clients who have been charged with a crime/DWI

Industry/Entity Type

legal

Font styles to use
Serif
Sans Serif

Requirements
Must have
• Needs to have the firm name in large lettering. Law Offices of Marcus T Whitfield. “PLLC” does not have to be included. Phone number of (555) 384-1927 should be included but not the main focus.
Nice to have
• A call to action or something similar. “Don’t go it alone, call today.”, “ Arrested?”

```html
<!DOCTYPE html>
<html lang="en">
<head>
<meta charset="UTF-8">
<title>Law Offices of Marcus T Whitfield — Billboard</title>
<link rel="stylesheet" href="https://fonts.googleapis.com/css2?family=Alfa+Slab+One&family=Anton&family=Poppins:wght@500;600;700;800&display=swap">
<style>
  :root {
    --navy-deep: #071a5c;
    --navy: #0a2a8f;
    --blue: #1247d6;
    --blue-bright: #2f7dff;
    --streak: #7fd3ff;
    --gold: #ffb81a;
    --gold-light: #ffe100;
    --white: #ffffff;
    --ink: #13237a;
    --badge-fill: #1c2a5e;
  }
  html, body {
    margin: 0;
    padding: 0;
    width: 1200px;
    height: 350px;
    overflow: hidden;
    background: var(--navy-deep);
  }
  .billboard {
    position: relative;
    width: 1200px;
    height: 350px;
    overflow: hidden;
    background:
      radial-gradient(ellipse at 30% 20%, rgba(47,125,255,0.55), transparent 55%),
      linear-gradient(100deg, var(--navy-deep) 0%, var(--blue) 35%, var(--navy) 70%, var(--navy-deep) 100%);
    font-family: "Poppins", sans-serif;
  }
  .streaks {
    position: absolute;
    inset: 0;
  }
  .attorney-portrait {
    position: absolute;
    left: 0;
    top: 36px;
    width: 322px;
    height: 314px;
    background: linear-gradient(160deg, #bdbdbd 0%, #7c7c7c 45%, #3d3d3d 100%);
    clip-path: polygon(28% 0, 70% 0, 76% 38%, 92% 48%, 100% 100%, 0 100%, 0 44%, 24% 36%);
  }
  .firm-prefix {
    position: absolute;
    left: 406px;
    top: 32px;
    margin: 0;
    font-family: "Alfa Slab One", serif;
    font-weight: 400;
    font-size: 52px;
    line-height: 1;
    letter-spacing: 1px;
    background: linear-gradient(90deg, var(--gold) 0%, var(--gold-light) 45%, var(--gold) 100%);
    -webkit-background-clip: text;
    background-clip: text;
    color: transparent;
  }
  .firm-name {
    position: absolute;
    left: 303px;
    top: 96px;
  }
  .firm-name text {
    font-family: "Anton", sans-serif;
    fill: var(--white);
  }
  .award-badge {
    position: absolute;
    left: 1028px;
    top: 0;
    width: 132px;
    height: 216px;
    border-radius: 0 0 6px 6px;
    background: var(--badge-fill);
  }
  .cta-question {
    position: absolute;
    left: 332px;
    top: 244px;
    margin: 0;
    font-family: "Poppins", sans-serif;
    font-weight: 800;
    font-size: 35px;
    line-height: 1;
    letter-spacing: -0.5px;
    color: var(--gold);
  }
  .cta-band {
    position: absolute;
    left: 303px;
    top: 284px;
    width: 501px;
    height: 49px;
    background: var(--white);
    clip-path: polygon(0 0, 95% 0, 100% 100%, 0 100%);
  }
  .cta-line {
    position: absolute;
    left: 328px;
    top: 288px;
    margin: 0;
    font-weight: 700;
    font-size: 31px;
    line-height: 42px;
    letter-spacing: -0.6px;
    color: var(--ink);
  }
  .contact {
    position: absolute;
    right: 114px;
    top: 256px;
    text-align: right;
    color: var(--white);
    font-style: normal;
  }
  .contact-name {
    margin: 0 0 3px;
    font-weight: 600;
    font-size: 19px;
    line-height: 1.1;
    letter-spacing: 0.2px;
  }
  .contact-row {
    display: flex;
    justify-content: flex-end;
    align-items: flex-start;
    gap: 5px;
    margin: 0 0 3px;
    font-weight: 600;
    font-size: 10px;
    line-height: 12px;
  }
  .contact-row svg {
    flex: none;
  }
  .attorney-headshot {
    position: absolute;
    left: 1096px;
    top: 237px;
    width: 58px;
    height: 89px;
    border: 2px solid var(--white);
    background: linear-gradient(180deg, #5a3a2a 0%, #8a6a55 40%, #556070 75%, #3b4555 100%);
  }
</style>
</head>
<body>
<div class="billboard">

  <svg class="streaks" width="1200" height="350" viewBox="0 0 1200 350" aria-hidden="true">
    <defs>
      <linearGradient id="streakGlow" x1="0" y1="0" x2="1" y2="1">
        <stop offset="0" stop-color="#7fd3ff" stop-opacity="0"/>
        <stop offset="0.5" stop-color="#7fd3ff" stop-opacity="0.9"/>
        <stop offset="1" stop-color="#7fd3ff" stop-opacity="0"/>
      </linearGradient>
    </defs>
    <polygon points="120,0 260,0 700,350 560,350" fill="#2f7dff" opacity="0.18"/>
    <polygon points="380,0 470,0 910,350 820,350" fill="#2f7dff" opacity="0.14"/>
    <line x1="230" y1="0" x2="700" y2="340" stroke="url(#streakGlow)" stroke-width="2.5"/>
    <line x1="330" y1="0" x2="820" y2="350" stroke="url(#streakGlow)" stroke-width="1.2" opacity="0.6"/>
    <line x1="160" y1="40" x2="620" y2="350" stroke="#7fd3ff" stroke-width="1" opacity="0.35"/>
    <line x1="560" y1="0" x2="1000" y2="320" stroke="#7fd3ff" stroke-width="1" opacity="0.3"/>
    <circle cx="268" cy="30" r="7" fill="#bfe9ff" opacity="0.85"/>
    <polygon points="380,190 560,190 705,250 530,250" fill="#1a5cff" opacity="0.25"/>
  </svg>

  <div class="attorney-portrait" role="img" aria-label="Black and white photo of the attorney in a suit vest and tie, jacket over his shoulder"></div>

  <h1 class="firm-prefix">LAW OFFICES OF</h1>

  <svg class="firm-name" width="670" height="112" viewBox="0 0 670 112" role="img" aria-label="Marcus T Whitfield">
    <text x="2" y="109" font-size="140" textLength="662" lengthAdjust="spacingAndGlyphs">MARCUS T WHITFIELD</text>
  </svg>

  <div class="award-badge" role="img" aria-label="Community award badge"></div>

  <p class="cta-question">Arrested?</p>
  <div class="cta-band"></div>
  <p class="cta-line">Don’t go it alone, call today.</p>

  <address class="contact">
    <p class="contact-name">Marcus T. Whitfield</p>
    <p class="contact-row">(555) 384-1927
      <svg width="12" height="12" viewBox="0 0 12 12" aria-hidden="true"><path d="M1 1h10v6.5L6 11.5 1 7.5z" fill="#fff"/><path d="M4 3.2l1 1-.6.8c.4.8 1 1.4 1.8 1.8l.8-.6 1 1-.7.9C5.6 7.8 4.2 6.4 3.6 4z" fill="#0a2a8f"/></svg>
    </p>
    <p class="contact-row">mtwhitfieldlaw@example.com
      <svg width="12" height="12" viewBox="0 0 12 12" aria-hidden="true"><path d="M1 1h10v6.5L6 11.5 1 7.5z" fill="#fff"/><rect x="3" y="3.3" width="6" height="4" fill="none" stroke="#0a2a8f" stroke-width="0.9"/><path d="M3 3.5l3 2.2 3-2.2" fill="none" stroke="#0a2a8f" stroke-width="0.9"/></svg>
    </p>
    <p class="contact-row">218 N. Larkspur Avenue<br>Millbrook, Arkansas 72950
      <svg width="12" height="12" viewBox="0 0 12 12" aria-hidden="true"><path d="M1 1h10v6.5L6 11.5 1 7.5z" fill="#fff"/><path d="M6 2.8a2 2 0 0 1 2 2c0 1.4-2 3.4-2 3.4s-2-2-2-3.4a2 2 0 0 1 2-2z" fill="#0a2a8f"/></svg>
    </p>
  </address>

  <div class="attorney-headshot" role="img" aria-label="Color headshot of the attorney in a grey suit, smiling outdoors"></div>

</div>
</body>
</html>
```